Professional Learning Organization for Educators needs a Design Thinking Workshop Flyer

We need a flyer for a series of Introductory Design Thinking workshops we're delivering for education leaders.

We have generated our own version of the flyer with a word template, but want it to look even more professional and eye catching. It is attached.

We had an image that we thought might be good, but pulled it out so we don't bias designers' thinking.
Updates

Reason: We are a bit flexible on the deadline since this is a holiday week and people are traveling

Target Market(s)

Very busy education leaders whose curiosity needs to be stimulated enough to enroll in the course

Industry/Entity Type

Education

Font styles to use
Other font styles liked:
• Century Gothic or something closer to that

Requirements
Must have
• Some version of the text that is on the current flyer that I attached.
Nice to have
• I am very flexible and open right now on this design.

```html
<!DOCTYPE html>
<html lang="en">
<head>
<meta charset="UTF-8">
<title>Design Thinking Workshops Flyer</title>
<link rel="stylesheet" href="https://fonts.googleapis.com/css2?family=Roboto+Condensed:wght@400;700&family=Roboto:wght@400;500;700&display=swap">
<style>
  :root {
    --red: #e31e2b;
    --red-dark: #b3121c;
    --blue: #1a86b8;
    --blue-deep: #0d4a70;
    --navy: #113a5c;
    --white: #ffffff;
    --ink: #2b2b2b;
    --stage: #e8e5e1;
  }
  * { margin: 0; padding: 0; box-sizing: border-box; }
  html, body { width: 1200px; height: 1200px; overflow: hidden; background: var(--stage); }
  .flyer {
    position: absolute; left: 160px; top: 30px; width: 880px; height: 1140px;
    overflow: hidden; background: var(--white);
    font-family: "Roboto", Arial, sans-serif; color: var(--white);
    box-shadow: 0 6px 24px rgba(0,0,0,.18);
  }
  .flyer-bg { position: absolute; inset: 0; }
  .brand {
    position: absolute; right: 50px; top: 92px; display: flex; align-items: center; gap: 12px;
    font-family: "Roboto Condensed", Arial, sans-serif; font-weight: 700;
    font-size: 46px; line-height: 1; color: var(--red); text-align: right;
  }
  .brand-dot { width: 22px; height: 22px; border-radius: 50%; background: var(--blue); }
  .title {
    position: absolute; right: 32px; top: 238px; text-align: right;
    font-family: "Roboto Condensed", Arial, sans-serif; font-weight: 700;
    font-size: 47px; line-height: 52px; letter-spacing: .3px;
  }
  .title-blue { color: var(--blue); display: block; }
  .title-red { color: var(--red); display: block; }
  .ribbon {
    position: absolute; left: 0; top: 508px; width: 477px; height: 40px;
    background: linear-gradient(180deg, #f0303c, var(--red-dark));
    border-radius: 0 20px 20px 0;
    font-family: "Roboto Condensed", Arial, sans-serif; font-weight: 700;
    font-size: 20.5px; line-height: 40px; padding-left: 50px; letter-spacing: .2px;
    box-shadow: 0 2px 4px rgba(0,0,0,.25);
  }
  .intro {
    position: absolute; left: 49px; top: 560px; width: 423px;
    font-size: 14px; line-height: 17.3px;
  }
  .intro p { text-align: justify; }
  .benefits { list-style: none; margin: 6px 0 8px; }
  .benefits li { position: relative; padding-left: 33px; margin-bottom: 8px; }
  .benefits li::before {
    content: ""; position: absolute; left: 4px; top: 5px; width: 8px; height: 8px;
    border-radius: 50%; background: var(--red);
  }
  .schedule {
    list-style: none; margin-top: 10px;
    font-family: "Roboto Condensed", Arial, sans-serif; font-weight: 700; font-size: 17.5px;
  }
  .schedule li { display: flex; align-items: center; gap: 14px; height: 27.5px; }
  .tick { width: 15px; height: 13px; flex: none; }
  .testimonials {
    position: absolute; left: 517px; top: 397px; width: 305px; height: 517px;
    background: linear-gradient(160deg, #ee2a36 0%, var(--red) 45%, var(--red-dark) 100%);
    border-radius: 22px; text-align: center; padding: 22px 16px 0;
    box-shadow: 0 4px 10px rgba(0,0,0,.3);
  }
  .panel-heading, .panel-org, .panel-question {
    font-family: "Roboto Condensed", Arial, sans-serif; font-weight: 700;
    font-size: 23.5px; line-height: 30px;
  }
  .quote { font-size: 13.6px; line-height: 17px; margin-top: 10px; }
  .divider { width: 100px; height: 2px; background: var(--white); margin: 12px auto 0; opacity: .9; }
  .panel-org { margin-top: 20px; }
  .panel-link { font-size: 17.5px; line-height: 24px; }
  .panel-question { margin-top: 18px; }
  .enroll {
    position: absolute; left: 0; right: 0; top: 988px; text-align: center;
    font-family: "Roboto Condensed", Arial, sans-serif; font-size: 27px; line-height: 35px; color: var(--red);
  }
  .enroll .url { color: var(--blue); }
  .notes {
    position: absolute; left: 0; right: 0; top: 1061px; text-align: center;
    font-size: 16.5px; line-height: 27px; color: var(--ink); font-weight: 500;
  }
  .notes span { display: inline-block; position: relative; padding-left: 26px; margin: 0 18px; }
  .notes span::before {
    content: ""; position: absolute; left: 4px; top: 10px; width: 8px; height: 8px;
    border-radius: 50%; background: var(--blue);
  }
</style>
</head>
<body>
<main class="flyer">
  <svg class="flyer-bg" viewBox="0 0 880 1140" width="880" height="1140">
    <defs>
      <linearGradient id="paper" x1="0" y1="0" x2="1" y2="1">
        <stop offset="0" stop-color="#ffffff"/><stop offset="1" stop-color="#ececec"/>
      </linearGradient>
      <linearGradient id="sea" x1="0" y1="0" x2="0.3" y2="1">
        <stop offset="0" stop-color="#0d4a70"/><stop offset="0.5" stop-color="#1b8cbf"/><stop offset="1" stop-color="#0f5d88"/>
      </linearGradient>
      <radialGradient id="photo" cx="0.5" cy="0.5" r="0.6">
        <stop offset="0" stop-color="#f2e6c8"/><stop offset="0.2" stop-color="#3f9ad6"/>
        <stop offset="0.6" stop-color="#173f78"/><stop offset="1" stop-color="#0a1f45"/>
      </radialGradient>
    </defs>
    <rect width="880" height="1140" fill="url(#paper)"/>
    <path d="M0,470 C150,520 340,505 470,440 C570,410 720,445 880,500 L880,1060 C720,990 540,955 420,956 C260,958 110,1005 0,1050 Z" fill="url(#sea)"/>
    <path d="M380,452 C520,425 720,440 880,480" fill="none" stroke="var(--red)" stroke-width="10"/>
    <path d="M0,1050 C110,1005 260,958 420,956 C540,955 720,990 880,1060" fill="none" stroke="var(--red)" stroke-width="9"/>
    <circle cx="200" cy="205" r="268" fill="var(--white)"/>
    <circle cx="200" cy="205" r="260" fill="none" stroke="var(--red)" stroke-width="10"/>
    <circle cx="200" cy="205" r="248" fill="none" stroke="var(--navy)" stroke-width="12"/>
    <circle cx="200" cy="205" r="239" fill="none" stroke="var(--red)" stroke-width="4"/>
    <circle cx="200" cy="205" r="237" fill="url(#photo)" role="img" aria-label="Photo of a hand reaching toward floating blue cubes with one glowing orange cube"/>
  </svg>

  <div class="brand"><span>FIELD DAY<br>STUDIO</span><span class="brand-dot"></span></div>

  <h1 class="title"><span class="title-blue">DESIGN THINKING</span><span class="title-red">WORKSHOPS</span></h1>

  <h2 class="ribbon">DESIGNING YOUR WAY TO BETTER SOLUTIONS</h2>

  <section class="intro">
    <p>Ridgeview Public Schools and Summit Valley Cooperative invite you to discover the power of Design Thinking. During our three session course, you will learn and practice mindsets and tools that help you continuously and creatively improve the experiences of the people you serve by:</p>
    <ul class="benefits">
      <li>Understanding what your teachers, students and community truly need in their learning and work experiences</li>
      <li>Designing solutions that better meet their needs</li>
      <li>Seeking authentic feedback and reactions to these solutions prior to their implementation.</li>
    </ul>
    <p>We are offering this three-session course at four different times in spring semester. Please choose the course that works best for your schedule.</p>
    <ul class="schedule">
      <li><svg class="tick" viewBox="0 0 15 13"><path d="M1,7 L5.5,11 L14,1.5" fill="none" stroke="var(--red)" stroke-width="3"/></svg>Monday mornings: 1/23, 1/30 and 2/6</li>
      <li><svg class="tick" viewBox="0 0 15 13"><path d="M1,7 L5.5,11 L14,1.5" fill="none" stroke="var(--red)" stroke-width="3"/></svg>Tuesday afternoons: 2/7, 2/14 and 2/21</li>
      <li><svg class="tick" viewBox="0 0 15 13"><path d="M1,7 L5.5,11 L14,1.5" fill="none" stroke="var(--red)" stroke-width="3"/></svg>Wednesday afternoons: 3/8, 3/15 and 3/22</li>
      <li><svg class="tick" viewBox="0 0 15 13"><path d="M1,7 L5.5,11 L14,1.5" fill="none" stroke="var(--red)" stroke-width="3"/></svg>Wednesday evenings: 2/8, 2/15 and 2/22</li>
    </ul>
  </section>

  <aside class="testimonials">
    <h3 class="panel-heading">WHAT OUR<br>PARTICIPANTS SAY...</h3>
    <p class="quote">“This has been an empowering experience that allowed me to try out dramatic changes in my practice that I wouldn't have imagined before.”</p>
    <div class="divider"></div>
    <p class="quote">“I never realized how often I've guessed and assumed what our teachers and students need – now I have a way to stop guessing!”</p>
    <div class="divider"></div>
    <p class="quote">“I finally have tools to generate truly creative ideas that people actually embrace... because they meet their needs”</p>
    <p class="panel-org">SUMMIT VALLEY COOP</p>
    <p class="panel-link">www.svcoop.org</p>
    <p class="panel-question">QUESTIONS?</p>
    <p class="panel-link">j.carter@svcoop.org</p>
  </aside>

  <div class="enroll">
    <p>Click here to enroll.</p>
    <p>Go to <span class="url">www.svcoop.org</span> to learn more.</p>
  </div>

  <div class="notes">
    <p><span>This course is held in Ridgeview Public Schools.</span><span>No fee for RPS leaders</span></p>
    <p><span>$150 fee for leaders outside of RPS.</span></p>
  </div>
</main>
</body>
</html>
```